Webdesign für Vernetzung christlicher Geschäftsleute
Zielgruppe
Die Vereinigung KRTWLE bezweckt die Vernetzung christlicher Geschäftsleute und die Verbreitung von Biblisch fundierten ethischen Geschäftsprinzipien. Die Zielgruppe umfasst Unternehmer und Verantwortungsträger aus Wirtschaft und Politik.
Aufgabenstellung
Ich suche einen Designer, welcher sich ernsthaft mit den Anforderungen und dem Design auseinandersetzt und eine Individuelle Lösung gestaltet.
Das Logo sowie ein unverbindlicher Vorschlag für die Strukturierung liegen bei.
Bitte keine 08/15 Business Stock Fotos (Händeschütteln, Meetings, Präsentationen).
Das Design soll folgende Seiten beinhalten (Beschreibung folgt):
- Startseite
- Standardseite (Titel, Text mit Bildern)
- Event-Detail Seite (Titel, Ort, Datum, ev. Foto, Beschreibungstext, ev. Map)
- Chapter Startseite
Die bestehende Webseite ist kein Massstab ;).

```html
<!DOCTYPE html>
<html lang="de">
<head>
<meta charset="utf-8">
<title>KRTWLE – Start</title>
<link rel="stylesheet" href="https://fonts.googleapis.com/css2?family=Open+Sans:wdth,wght@75..100,400..800&display=swap">
<style>
  :root {
    --ink: #111111;
    --red: #b3122a;
    --white: #ffffff;
    --band: #ececec;
    --text-grey: #555555;
    --photo-light: #f4f3f3;
    --photo-mid: #c9c7c8;
    --photo-dark: #6f6e70;
  }
  * { margin: 0; padding: 0; box-sizing: border-box; }
  html, body { width: 1200px; height: 800px; overflow: hidden; }
  body {
    position: relative;
    background: var(--white);
    font-family: "Open Sans", Arial, sans-serif;
    font-stretch: 75%;
    color: var(--ink);
  }
  .grey-band {
    position: absolute; left: 0; top: 470px; width: 1200px; height: 330px;
    background: var(--band);
  }
  .brand {
    position: absolute; left: 150px; top: 58px;
    display: flex; align-items: center; gap: 10px;
    font-weight: 800; font-size: 30px; color: var(--red); letter-spacing: 1px;
  }
  .brand-dot {
    width: 22px; height: 22px; border-radius: 50%; background: var(--red);
  }
  .main-nav {
    position: absolute; top: 42px; left: 640px;
    display: flex; gap: 74px;
    font-weight: 700; font-size: 16px; text-transform: uppercase;
  }
  .main-nav a { color: var(--ink); text-decoration: none; padding-bottom: 5px; }
  .main-nav a.is-active { border-bottom: 3px solid var(--red); }
  .hero-photo {
    position: absolute; left: 330px; top: 118px; width: 700px; height: 452px;
    background:
      radial-gradient(ellipse 60% 40% at 52% 45%, var(--photo-dark) 0%, var(--photo-mid) 45%, transparent 75%),
      linear-gradient(180deg, var(--photo-mid) 0%, var(--photo-light) 35%, var(--photo-light) 60%, var(--white) 100%);
    box-shadow: 0 8px 22px rgba(0,0,0,0.12);
  }
  .chapter-menu {
    position: absolute; left: 932px; top: 140px;
    display: flex; align-items: center; gap: 10px;
    font-weight: 700; font-size: 14px; text-transform: uppercase;
  }
  .hero-headline {
    position: absolute; left: 232px; top: 262px;
    display: flex; flex-direction: column; align-items: flex-start; gap: 10px;
  }
  .hero-headline span {
    background: var(--white);
    padding: 2px 10px 2px 8px;
    font-weight: 700; font-size: 46px; line-height: 58px; text-transform: uppercase;
  }
  .welcome {
    position: absolute; left: 252px; top: 640px; width: 480px;
  }
  .section-title {
    color: var(--red); font-weight: 700; font-size: 30px; text-transform: uppercase;
  }
  .welcome p {
    margin-top: 18px; font-size: 14px; line-height: 22px; color: var(--text-grey);
    font-stretch: 100%;
  }
  .chapters {
    position: absolute; left: 830px; top: 596px; width: 280px;
  }
  .chapter-thumb {
    margin-top: 14px; width: 270px; height: 150px;
    background: linear-gradient(160deg, #dcdcdc 0%, #a9a9ab 60%, #8b8b8d 100%);
  }
</style>
</head>
<body>
  <div class="grey-band"></div>

  <div class="brand"><span class="brand-dot"></span>KRTWLE</div>

  <nav class="main-nav">
    <a href="#" class="is-active">Start</a>
    <a href="#">Über uns</a>
    <a href="#">Kontakt</a>
  </nav>

  <div class="hero-photo" role="img" aria-label="Schneebedeckter Berggipfel in Wolken"></div>

  <div class="chapter-menu">Chapter
    <svg width="20" height="16" viewBox="0 0 20 16" aria-hidden="true">
      <rect y="0" width="20" height="3" fill="#111"/>
      <rect y="6.5" width="20" height="3" fill="#111"/>
      <rect y="13" width="20" height="3" fill="#111"/>
    </svg>
  </div>

  <h1 class="hero-headline">
    <span>Sein</span>
    <span>Zeichen</span>
    <span>Über uns</span>
    <span>ist Liebe</span>
  </h1>

  <section class="welcome">
    <h2 class="section-title">Willkommen</h2>
    <p>Lorem ipsum dolor sit amet, consetetur sadipscing elitr, sed diam nonumy eirmod tempor invidunt ut labore et dolore magna aliquyam erat, sed diam voluptua. At vero eos et accusam et justo duo dolores et ea rebum.</p>
  </section>

  <section class="chapters">
    <h2 class="section-title">Chapters</h2>
    <div class="chapter-thumb" role="img" aria-label="Bild eines regionalen Chapters"></div>
  </section>
</body>
</html>
```